Business card design needed

I would like to use the print I have supplied with my Logo & info i have supplied.
On the back i would like a
*We Use & Recommend*
*Tarvin Filters
*Dulmok Oils
*QRV Spark Plugs
*Z-Blade Exhaust
*Colvane Brake Pads

*Your Next Appointment:

Industry/Entity Type

Business

Contact Information for Business Card

FERRIMS AUTO CENTRE
All Mechanical Repairs
Log Book Servicing
Authorised NSW Inspection station
Email: ferrimsautocentre@mailbox-example.com.au
17 Tumbrel Rd
P.O.Box 8270
Queanbeyan NSW 2629
0262480315

```html
<!DOCTYPE html>
<html lang="en">
<head>
<meta charset="utf-8">
<title>Ferrims Auto Centre – Business Card</title>
<link rel="stylesheet" href="https://fonts.googleapis.com/css2?family=Cabin:wght@500;700&display=swap">
<style>
  :root {
    --paper: #ffffff;
    --ink: #333333;
    --brand-red: #d5353c;
    --brand-blue: #17b1e7;
    --on-colour: #ffffff;
  }
  * { margin: 0; padding: 0; box-sizing: border-box; }
  html, body {
    width: 1200px;
    height: 1000px;
    overflow: hidden;
    background: var(--paper);
  }
  .card {
    position: relative;
    width: 1200px;
    height: 1000px;
    background: var(--paper);
    font-family: "Cabin", sans-serif;
    font-weight: 500;
    color: var(--ink);
  }
  .contact-phone {
    position: absolute;
    left: 120px;
    top: 236px;
    font-size: 28px;
    line-height: 38px;
  }
  .contact-address {
    position: absolute;
    right: 110px;
    top: 236px;
    font-size: 28px;
    line-height: 37px;
    text-align: right;
    font-style: normal;
  }
  .brand-band {
    position: absolute;
    left: 104px;
    top: 385px;
    width: 992px;
    height: 203px;
    background: var(--brand-red);
    display: flex;
    align-items: center;
    justify-content: center;
  }
  .brand-name {
    color: var(--on-colour);
    font-weight: 700;
    font-size: 64px;
    letter-spacing: 2px;
  }
  .services {
    position: absolute;
    left: 0;
    top: 605px;
    width: 1200px;
    list-style: none;
    text-align: center;
    font-size: 29px;
    line-height: 37px;
  }
  .email-band {
    position: absolute;
    left: 104px;
    top: 731px;
    width: 992px;
    height: 41px;
    background: var(--brand-blue);
    color: var(--on-colour);
    font-size: 29px;
    line-height: 41px;
    text-align: center;
  }
</style>
</head>
<body>
  <main class="card">
    <p class="contact-phone">Call: 2629 0262480315</p>
    <address class="contact-address">
      17 Tumbrel Rd, P.O.Box 8270<br>
      Queanbeyan, NSW
    </address>
    <div class="brand-band">
      <span class="brand-name">FERRIMS AUTO CENTRE</span>
    </div>
    <ul class="services">
      <li>All Mechanical Repairs</li>
      <li>Log Book Servicing</li>
      <li>Authorised NSW Inspection station</li>
    </ul>
    <p class="email-band">Email: ferrimsautocentre@mailbox-example.com.au</p>
  </main>
</body>
</html>
```